SKYVANTEX (drone photo and video) and Photogrammetry Services (mapping and 3D modeling)

We need a business card design for a SKYVANTEX. Our businesses provides (drone) Aerial Photo and Video Captures. However we also provide Photogrammetry (which is 3D modeling and mapping). We greatly value unique points of view taken of landscapes and subjects with aerial photography and videography. 3D modeling and mapping is the other area of focus and have an incredibly broad scope of applications and imaginative creativity.

Target Market(s)

Based out of Northern Virginia and serving the greater Virginia and Maryland areas

Industry/Entity Type

Drone Photo and video and Photogrammetry Services (mapping and 3D modeling)

Contact Information for Business Card

3D Models, Maps and Photo/Video Production name: Marcus Pettibone email: mqp@skyvantex.us website: skyvantex.us phone: 571-806-3394; please also include "Aerial Photo/Video and 3D Mapping/Modeling"

Requirements
Must have
• Please make this design vertical and double sided. The selection box is not letting me choose Double Sided but that is my wish. Incorporate uploaded LOGO and color scheme
Nice to have
• Preferably does not feel too crowded and balances not having an exaggerated amount of distracting detail
Should not have
• do not cram bullet points or text in long form

```html
<!DOCTYPE html>
<html lang="en">
<head>
<meta charset="utf-8">
<title>SKYVANTEX Business Card</title>
<link rel="stylesheet" href="https://fonts.googleapis.com/css2?family=Montserrat:wght@700&family=Oswald:wght@300;400;500&display=swap">
<style>
  :root {
    --backdrop: #d0d0d0;
    --card: #ffffff;
    --ink: #111111;
    --brand-red: #f5202a;
    --brand-orange: #ff6a1a;
    --grad-warm: #fdb21f;
    --grad-mid: #ff7f22;
    --grad-hot: #ff3b24;
    --muted: #666666;
    --tagline: #b5b5b5;
  }
  * { margin: 0; padding: 0; box-sizing: border-box; }
  html, body {
    width: 1200px; height: 1000px; overflow: hidden;
    background: var(--backdrop);
  }
  .stage { position: relative; width: 1200px; height: 1000px; }
  .card {
    position: absolute; top: 187px;
    width: 353px; height: 613px;
    background: var(--card);
    border-radius: 28px;
    overflow: hidden;
  }
  .card--front { left: 222px; }
  .card--back { left: 620px; }

  .front-hero {
    position: absolute; left: 0; top: 0;
    width: 100%; height: 423px;
    background: linear-gradient(45deg, var(--grad-warm) 0%, var(--grad-mid) 45%, var(--grad-hot) 100%);
  }
  .front-name {
    position: absolute; left: 0; right: 0; top: 470px;
    text-align: center;
    font-family: "Montserrat", sans-serif;
    font-weight: 700; font-size: 46px; letter-spacing: 1px;
    color: var(--ink);
  }

  .back-mark {
    position: absolute; left: 50%; top: 48px;
    width: 70px; height: 70px; margin-left: -35px;
    border-radius: 50%;
    background: var(--brand-orange);
  }
  .back-name {
    position: absolute; left: 0; right: 0; top: 138px;
    text-align: center;
    font-family: "Montserrat", sans-serif;
    font-weight: 700; font-size: 30px; letter-spacing: 1px;
    color: var(--ink);
  }
  .tagline {
    position: absolute; left: 0; right: 0; top: 176px;
    text-align: center;
    font-family: "Oswald", sans-serif;
    font-weight: 400; font-size: 12.5px;
    color: var(--tagline);
  }
  .person {
    position: absolute; left: 50%; top: 285px;
    transform: translateX(-50%);
    padding: 8px 2px;
    border-top: 4px solid var(--brand-red);
    border-bottom: 4px solid var(--brand-red);
    font-family: "Oswald", sans-serif;
    font-weight: 500; font-size: 30px; line-height: 42px;
    color: var(--brand-red);
    white-space: nowrap;
  }
  .contact {
    position: absolute; left: 0; right: 0; top: 395px;
    text-align: center;
    font-family: "Oswald", sans-serif;
    font-weight: 300; font-size: 22px; line-height: 30px;
    color: var(--muted);
  }
  .phone {
    position: absolute; left: 0; right: 0; top: 486px;
    text-align: center;
    font-family: "Oswald", sans-serif;
    font-weight: 400; font-size: 21px;
    color: var(--brand-red);
  }
</style>
</head>
<body>
  <main class="stage">
    <section class="card card--front">
      <div class="front-hero" role="img" aria-label="Illustration of a drone flying above snowy mountain peaks on a warm orange gradient"></div>
      <p class="front-name">SKYVANTEX</p>
    </section>

    <section class="card card--back">
      <div class="back-mark"></div>
      <p class="back-name">SKYVANTEX</p>
      <p class="tagline">Aerial Photo/Video and 3D Mapping/Modeling</p>
      <p class="person">MARCUS PETTIBONE</p>
      <p class="contact">mqp@skyvantex.us<br>skyvantex.us</p>
      <p class="phone">571-806-3394</p>
    </section>
  </main>
</body>
</html>
```